Back Pain

Need a flyer similar to the attached draft. This is to be handed out to prospective patients. Note that Sketch Hive has already designed the logo. If you need a copy please contact me

```html
<!DOCTYPE html>
<html lang="en">
<head>
<meta charset="utf-8">
<title>Spine Ease Clinic – Flyer</title>
<link href="https://fonts.googleapis.com/css2?family=Bebas+Neue&family=Poppins:wght@400;600&display=swap" rel="stylesheet">
<style>
  :root {
    --green: #7dc242;
    --blue: #1a72bf;
    --ink: #0d0d0d;
    --paper: #ffffff;
    --backdrop: #d9d9d9;
    --silhouette: #151515;
  }
  * { box-sizing: border-box; margin: 0; padding: 0; }
  html, body { width: 1200px; height: 967px; overflow: hidden; background: var(--backdrop); }
  .flyer {
    position: absolute; left: 280px; top: 31px; width: 640px; height: 905px;
    background: var(--paper); overflow: hidden;
    font-family: "Bebas Neue", "Oswald", sans-serif;
  }
  .title {
    position: absolute; right: 26px; top: 26px;
    font-size: 66px; color: var(--green); letter-spacing: 1px; line-height: 1;
  }
  .figure {
    position: absolute; left: 24px; top: 112px; width: 218px; height: 360px;
    background: linear-gradient(180deg, #2a2a2a, var(--silhouette));
    border-radius: 40px 40px 8px 8px;
  }
  .symptoms { position: absolute; left: 230px; top: 140px; list-style: none; }
  .symptoms li {
    height: 26px; margin-bottom: 8px; background: var(--blue); color: var(--green);
    font-size: 24px; line-height: 28px; text-align: right; padding-right: 10px;
  }
  .chart { position: absolute; left: 432px; top: 150px; width: 200px; height: 210px; }
  .chart-caption {
    position: absolute; left: 0; top: 0; width: 190px;
    color: var(--green); font-size: 15px; line-height: 1.05;
  }
  .chart svg { position: absolute; left: 0; top: 40px; }
  .devices { position: absolute; left: 318px; top: 372px; width: 310px; height: 70px; }
  .devices svg { position: absolute; left: 0; top: 0; }
  .devices-text {
    position: absolute; left: 78px; top: 6px; font-size: 16px; line-height: 1; color: var(--ink);
  }
  .devices-text strong { font-weight: 400; font-size: 28px; color: var(--ink); }
  .devices-text strong .hl { color: var(--blue); }
  .headline {
    position: absolute; left: 36px; top: 462px; width: 590px;
    font-size: 41px; line-height: 44px; color: var(--ink); text-align: right;
  }
  .headline .blue { color: var(--blue); }
  .divider {
    position: absolute; left: 40px; right: 40px; top: 652px;
    border-top: 3px dotted var(--blue); opacity: .6;
  }
  .practitioner {
    position: absolute; left: 40px; top: 664px; width: 580px;
    font-family: "Poppins", sans-serif; font-size: 25px; line-height: 34px; color: var(--blue);
  }
  .practitioner .name { color: var(--green); font-weight: 600; }
  .brand { position: absolute; left: 30px; top: 770px; width: 170px; }
  .brand-mark { width: 34px; height: 34px; border-radius: 50%; background: var(--blue); margin-bottom: 6px; }
  .brand-name { font-family: "Poppins", sans-serif; font-weight: 600; font-size: 17px; color: var(--blue); line-height: 1.1; }
  .brand-sub { font-family: "Poppins", sans-serif; font-weight: 600; font-size: 9px; color: var(--blue); letter-spacing: .5px; margin-top: 3px; }
  .offer { position: absolute; left: 214px; top: 752px; display: flex; align-items: flex-start; }
  .offer-amount { font-size: 100px; line-height: .9; color: var(--ink); }
  .offer-amount .pct { font-size: 46px; }
  .offer-amount .off { display: block; font-size: 36px; color: var(--green); margin-left: 92px; margin-top: -36px; }
  .offer-text {
    font-family: "Poppins", sans-serif; font-size: 15px; line-height: 22px; color: var(--ink);
    margin-left: 16px; margin-top: 6px; width: 260px;
  }
  .offer-text .url { color: var(--green); font-weight: 600; }
  .offer-note { display: block; font-size: 12px; margin-top: 6px; text-align: right; }
  .offer-note b { font-weight: 600; }
  .band {
    position: absolute; left: 0; right: 0; bottom: 0; height: 22px;
    background: linear-gradient(90deg, var(--green), var(--blue));
  }
</style>
</head>
<body>
<main class="flyer">
  <h1 class="title">SPINE EASE CLINIC</h1>

  <div class="figure" role="img" aria-label="Silhouette of a man walking while looking down at his phone"></div>

  <ul class="symptoms">
    <li style="width:200px">Headaches</li>
    <li style="width:170px">Neck Pain</li>
    <li style="width:210px">Shoulder Pain</li>
    <li style="width:150px">Back Pain</li>
    <li style="width:200px">Arm &amp; Hand Pain</li>
    <li style="width:110px">Sciatica</li>
  </ul>

  <section class="chart">
    <p class="chart-caption">As the head tilts forward, more force is placed on the spine</p>
    <svg width="200" height="170" viewBox="0 0 200 170" font-family="Bebas Neue, sans-serif">
      <g fill="#1a72bf">
        <rect x="6" y="106" width="26" height="24"/>
        <rect x="38" y="76" width="26" height="54"/>
        <rect x="70" y="50" width="26" height="80"/>
        <rect x="102" y="32" width="26" height="98"/>
        <rect x="134" y="10" width="26" height="120"/>
      </g>
      <g fill="#7dc242" font-size="17" text-anchor="middle">
        <text x="19" y="126">12</text>
        <text x="51" y="126">27</text>
        <text x="83" y="126">40</text>
        <text x="115" y="126">49</text>
        <text x="147" y="126">60</text>
      </g>
      <g fill="#0d0d0d" font-size="13" text-anchor="middle">
        <text x="19" y="144">0°</text>
        <text x="51" y="144">15°</text>
        <text x="83" y="144">30°</text>
        <text x="115" y="144">45°</text>
        <text x="147" y="144">60°</text>
        <text x="82" y="160">Degrees of forward head tilt</text>
        <text transform="translate(178 70) rotate(-90)">Pressure on spine (lbs)</text>
      </g>
    </svg>
  </section>

  <section class="devices">
    <svg width="64" height="64" viewBox="0 0 64 64" aria-hidden="true">
      <path d="M32 0 A32 32 0 0 0 32 64 Z" fill="#7dc242"/>
      <path d="M32 0 A32 32 0 0 1 32 64 Z" fill="#1a72bf"/>
      <rect x="22" y="14" width="20" height="36" rx="3" fill="none" stroke="#fff" stroke-width="2.5"/>
      <circle cx="32" cy="45" r="1.6" fill="#fff"/>
    </svg>
    <p class="devices-text">The average person spends<br><strong><span class="hl">8-11</span> hours per day</strong><br>using electronic devices</p>
  </section>

  <h2 class="headline">
    Chiropractic care <span class="blue">can help</span><br>
    <span class="blue">correct and prevent these problems</span><br>
    <span class="blue">by</span> restoring and maintaining<br>
    proper alignment <span class="blue">of the</span> neck
  </h2>

  <div class="divider"></div>

  <p class="practitioner"><span class="name">Dr Oliver Hartley</span> Now in<br>Harbourside at 42 Quay St - Atrium Suites</p>

  <div class="brand">
    <div class="brand-mark"></div>
    <div class="brand-name">Spine Ease Clinic</div>
    <div class="brand-sub">DR OLLIE HARTLEY - CHIROPRACTOR</div>
  </div>

  <div class="offer">
    <div class="offer-amount">50<span class="pct">%</span><span class="off">OFF</span></div>
    <p class="offer-text">Initial Consultation if you book online at <span class="url">www.spineeaseclinic.com.au</span>
      <span class="offer-note">*Choose <b>“TECH NECK”</b> Option</span></p>
  </div>

  <div class="band"></div>
</main>
</body>
</html>
```